business card for a massage therapy practice named 'Meadow and Willow Massage Studio'

I really need a trendy, yet easy on the eyes business card to complement my logo. Ideally with some gold or rose gold foil work.

My uploaded file of the logo I have in horizontal but I have a vertical version as well. Another color that is used in the website is a blush pink here and there. I'd like to see some trendy tropical leaves in the design.

```html
<!DOCTYPE html>
<html lang="en">
<head>
<meta charset="utf-8">
<title>Meadow and Willow Massage Studio – Business Card</title>
<link href="https://fonts.googleapis.com/css2?family=Roboto:wght@400;500;700&display=swap" rel="stylesheet">
<style>
  :root {
    --page-bg: #ffffff;
    --ink: #111111;
    --brand-ink: #1c1c1c;
    --gold: #a8946a;
    --rose: #dba0ae;
    --jungle-dark: #0a201b;
    --jungle-mid: #1f4a3a;
    --jungle-leaf: #3f7a55;
    --blush: #f3c7dc;
    --mint: #84cfb4;
    --white: #ffffff;
  }
  * { box-sizing: border-box; margin: 0; padding: 0; }
  html, body {
    width: 1200px; height: 1040px; overflow: hidden;
    background: var(--page-bg);
    font-family: "Roboto", Arial, sans-serif;
    color: var(--ink);
  }
  .canvas { position: relative; width: 1200px; height: 1040px; }

  /* Brand name header */
  .brand-header {
    position: absolute; left: 388px; top: 62px; width: 440px;
    display: flex; align-items: center; gap: 18px;
  }
  .brand-header__dot {
    width: 54px; height: 54px; border-radius: 50%;
    background: var(--gold); flex: none;
  }
  .brand-header__name {
    font-weight: 500; font-size: 34px; line-height: 1.15;
    color: var(--brand-ink); letter-spacing: 0.5px;
  }

  /* Cards */
  .card { position: absolute; box-shadow: 0 6px 18px rgba(0,0,0,0.18); }

  .card--front {
    left: 270px; top: 305px; width: 424px; height: 242px;
    overflow: hidden;
  }
  .card__foliage {
    position: absolute; inset: 0;
    background:
      radial-gradient(ellipse 62% 52% at 50% 50%, var(--jungle-dark) 60%, transparent 100%),
      linear-gradient(135deg, var(--jungle-mid), var(--jungle-leaf) 45%, var(--jungle-mid) 70%, #5a2b36);
  }
  .card__brand {
    position: absolute; left: 0; right: 0; top: 50%;
    transform: translateY(-50%);
    text-align: center;
    font-weight: 500; font-size: 22px; line-height: 1.3;
    color: var(--rose); letter-spacing: 0.5px;
  }

  .card--back {
    left: 447px; top: 554px; width: 423px; height: 247px;
    background: var(--blush);
  }
  .appointment {
    position: absolute; left: 119px; top: 91px; width: 186px;
    border: 3px solid var(--mint);
  }
  .appointment__label {
    background: var(--white);
    font-size: 13.5px; font-weight: 500; text-align: center;
    padding: 7px 0 8px;
  }
  .appointment__phone {
    background: var(--mint);
    display: flex; align-items: center; justify-content: center; gap: 8px;
    font-size: 15px; font-weight: 700;
    padding: 6px 0 8px;
  }
  .appointment__phone svg { width: 13px; height: 13px; }

  .contact {
    position: absolute; left: 0; right: 0; top: 184px;
    text-align: center; font-size: 12.5px; line-height: 16px;
  }
  .contact__name { font-weight: 700; }
  .contact__links {
    display: flex; justify-content: center; align-items: center; gap: 6px;
  }
  .contact__links svg { width: 13px; height: 11px; }
  .contact__links .spacer { width: 12px; }
</style>
</head>
<body>
<main class="canvas">

  <header class="brand-header">
    <span class="brand-header__dot"></span>
    <span class="brand-header__name">Meadow and Willow<br>Massage Studio</span>
  </header>

  <section class="card card--front">
    <div class="card__foliage" role="img" aria-label="Dark tropical foliage pattern with palm leaves, lilies and burgundy leaves framing the card"></div>
    <div class="card__brand">Meadow and Willow<br>Massage Studio</div>
  </section>

  <section class="card card--back">
    <div class="appointment">
      <div class="appointment__label">Call or Text for appointment</div>
      <div class="appointment__phone">
        <svg viewBox="0 0 24 24" aria-hidden="true"><path fill="#111" d="M6.6 10.8a15.1 15.1 0 0 0 6.6 6.6l2.2-2.2a1 1 0 0 1 1-.25 11.4 11.4 0 0 0 3.6.57 1 1 0 0 1 1 1V20a1 1 0 0 1-1 1A17 17 0 0 1 3 4a1 1 0 0 1 1-1h3.5a1 1 0 0 1 1 1c0 1.25.2 2.45.57 3.57a1 1 0 0 1-.25 1z"/></svg>
        <span>(555) 214-0387</span>
      </div>
    </div>
    <div class="contact">
      <div class="contact__name">Meadow and Willow</div>
      <div>482 Linden Ave. suite 210, Fairview, CA 95000</div>
      <div class="contact__links">
        <svg viewBox="0 0 16 12" aria-hidden="true"><rect width="16" height="12" rx="1" fill="#111"/><path d="M1 1l7 5 7-5" stroke="#fff" stroke-width="1.3" fill="none"/></svg>
        <span>hello@meadowandwillow.com</span>
        <span class="spacer"></span>
        <svg viewBox="0 0 16 12" aria-hidden="true"><rect x="2.5" y="1" width="11" height="7.5" fill="none" stroke="#111" stroke-width="1.4"/><rect x="0" y="9.5" width="16" height="2" fill="#111"/></svg>
        <span>www.meadowandwillow.com</span>
      </div>
    </div>
  </section>

</main>
</body>
</html>
```